DAG - EXPO

We are a sport event orgnizer managing diffrent sport events. We would like to orgnize the kick off event of the season Dune Active Games expo will be the gathering point of all sports events happening in Kuwait.
The expected events like Marathons, Ironloop , Triathlons , Karting , Inline skates , BMX.

Target Market(s)
Target market are outdoor and sports enthusiast
Industry/Entity Type
Events
Requirements
Must have
- Name of the event Dune Active Games EXPO
Dates 4-5 October 2013
Location Palm Terrace
Instegram account and twitter Dunegames24
website www.tarvelo.com.kw
Logos of the events who will participate attached
Nice to have
- Facts:
10 Events
8 Sports
6 Locations
5000+ Participants
in 5 Months ( in big bold so it can be the highlight )

```html
<!DOCTYPE html>
<html lang="en">
<head>
<meta charset="utf-8">
<title>Dune Active Games Expo</title>
<link rel="stylesheet" href="https://fonts.googleapis.com/css2?family=Fredoka:wght@700&family=Kurale&family=Marcellus+SC&family=Comfortaa:wght@400&display=swap">
<style>
  :root {
    --teal-deep: #256a6a;
    --teal-mid: #5f9f9d;
    --teal-soft: #9cc6c3;
    --teal-pale: #d3e6e4;
    --court-blue: #4b84a0;
    --band: #2b6e6f;
    --white: #ffffff;
  }
  html, body { margin: 0; padding: 0; overflow: hidden; }
  body { background: var(--teal-pale); }
  .poster {
    position: relative;
    width: 790px;
    height: 1200px;
    overflow: hidden;
    background: radial-gradient(ellipse at 40% 65%, var(--teal-soft) 0%, var(--teal-mid) 55%, #4e8f8d 100%);
  }
  .poster::after {
    content: "";
    position: absolute; inset: 0;
    background: linear-gradient(160deg, transparent 45%, rgba(220,238,236,.55) 100%);
    pointer-events: none;
  }
  .court-photo {
    position: absolute; left: 0; top: 0;
    width: 790px; height: 560px;
    background: linear-gradient(160deg, var(--court-blue) 0%, #4f8ea0 30%, rgba(95,159,157,0) 70%);
    clip-path: polygon(0 0, 100% 0, 100% 5%, 0 72%);
    z-index: 1;
  }
  .court-line {
    position: absolute; left: 0; top: 263px;
    width: 700px; height: 3px;
    background: rgba(255,255,255,.75);
    transform: rotate(-22.3deg);
    transform-origin: left center;
    z-index: 1;
  }
  .title-line {
    position: absolute;
    margin: 0;
    font-family: "Fredoka", sans-serif;
    font-weight: 700;
    text-transform: uppercase;
    letter-spacing: .03em;
    line-height: 1;
    white-space: nowrap;
    transform: translate(-50%, -50%) rotate(-33deg);
    z-index: 2;
  }
  .title-line.main { color: var(--teal-deep); font-size: 86px; }
  .title-line.echo { color: rgba(37,106,106,.26); font-size: 108px; }
  .title-line.main.l1 { left: 322px; top: 312px; }
  .title-line.main.l2 { left: 372px; top: 372px; }
  .title-line.echo.l1 { left: 372px; top: 226px; }
  .title-line.echo.l2 { left: 408px; top: 400px; }
  .title { margin: 0; }

  .facts { position: absolute; inset: 0; z-index: 3; font-family: "Kurale", serif; color: var(--teal-deep); }
  .facts .in { position: absolute; left: 96px; top: 606px; font-size: 74px; line-height: 1; }
  .facts .five {
    position: absolute; left: 194px; top: 568px; font-size: 160px; line-height: 1;
    color: var(--white);
    -webkit-text-stroke: 6px var(--teal-deep);
    paint-order: stroke fill;
  }
  .facts .months {
    position: absolute; left: 304px; top: 638px;
    width: 172px;
    font-family: "Fredoka", sans-serif; font-weight: 700;
    font-size: 44px; line-height: 1; letter-spacing: 0;
    text-align: center;
    color: var(--teal-deep);
    text-shadow: 2px 0 0 #fff, -2px 0 0 #fff, 0 2px 0 #fff, 0 -2px 0 #fff;
    transform: translate(-50%, -50%) rotate(90deg);
  }
  .facts ul { list-style: none; margin: 0; padding: 0; position: absolute; left: 334px; top: 552px; }
  .facts li { font-size: 39px; line-height: 42.5px; text-transform: uppercase; }

  .when {
    position: absolute; z-index: 3; margin: 0;
    font-family: "Marcellus SC", serif; color: var(--teal-deep);
    font-size: 40px; line-height: 1;
  }
  .when.date { left: 68px; top: 842px; }
  .when.place { right: 83px; top: 876px; }

  .contact-band {
    position: absolute; left: 0; right: 0; top: 1051px; bottom: 0;
    background: var(--band); z-index: 4;
  }
  .contacts { list-style: none; margin: 0; padding: 0; position: absolute; left: 6px; top: 2px; }
  .contacts li {
    font-family: "Comfortaa", sans-serif; color: var(--white);
    font-size: 25px; height: 36px; display: flex; align-items: center; gap: 8px;
  }
  .contacts .dot { width: 24px; height: 24px; border-radius: 4px; background: var(--white); opacity: .85; }
  .partners { position: absolute; left: 0; top: 0; width: 790px; height: 149px; }
</style>
</head>
<body>
<main class="poster">
  <div class="court-photo" role="img" aria-label="Photo of an outdoor sports court with a ball, fading into the teal background"></div>
  <div class="court-line"></div>

  <span class="title-line echo l1" aria-hidden="true">Dune Active</span>
  <span class="title-line echo l2" aria-hidden="true">Games Expo</span>
  <h1 class="title">
    <span class="title-line main l1">Dune Active</span>
    <span class="title-line main l2">Games Expo</span>
  </h1>

  <section class="facts">
    <span class="in">IN</span>
    <span class="five">5</span>
    <span class="months">MONTHS</span>
    <ul>
      <li>10 Events</li>
      <li>8 Sports</li>
      <li>6 Location</li>
      <li>5000+ Participants</li>
    </ul>
  </section>

  <p class="when date">OCTOBER 4 &amp; 5 2013</p>
  <p class="when place">PALM TERRACE</p>

  <footer class="contact-band">
    <ul class="contacts">
      <li><span class="dot"></span>facebook.com/TarveloSport</li>
      <li><span class="dot"></span>Dunegames24</li>
      <li><span class="dot"></span>Dunegames24</li>
      <li><span class="dot"></span>www.tarvelo.com.kw</li>
    </ul>
    <svg class="partners" viewBox="0 0 790 149" aria-label="Participating event badges">
      <rect x="502" y="71" width="111" height="31" fill="#fff"/>
      <rect x="615" y="71" width="110" height="31" fill="#fff"/>
      <rect x="450" y="110" width="42" height="30" fill="#d8262e"/>
      <rect x="494" y="110" width="64" height="30" fill="#d8262e"/>
      <rect x="561" y="110" width="111" height="30" fill="#fff"/>
      <rect x="674" y="110" width="109" height="30" fill="#fff"/>
    </svg>
  </footer>
</main>
</body>
</html>
```